STYLISH

It will be a brochure that exemplifies a project to make a modern and avant-garde LEGAL MAGAZINE to "sell it" to the sponsors, it will be a legal niche magazine for lawyers. The style is of the type "The Drifting Pebble" of the lawyers, breaks scheme, more disruptive More alternative with innovative personality and that calls the attention. It will be a collection magazine, to look at the reception of the Legal Firms. For public between 27 and 45 years. The name of the Magazine will be EL FARO

Target Market(s)

Chilean Lawyers between 27 and 45 years old.

Industry/Entity Type

Legal

Logo Text

EL FARO

Font styles to use
Sans Serif

Colors

Designer to choose colors to be used in the design.

Requirements
Must have
• Must say the name of the Magazine EL FARO Elevate the lawyer by giving him a different "coolness". We make them look and feel cool Elevate the lawyer to a public figure. They have something important to say. Our covers reflect that. A lawyer's study in a rich, unique session. The lawyer should be at the center of all our sections. They always in the middle. They are our protagonists.
Nice to have
• Minimalist, cool, fine. 1. With the white border like MORDANTE MAGAZINE attached. 2. The cover must have the photograph with the pictures of the opposite attached .. 3. Name ok the magazine: THE BEACON 4. On the left footer the word: COLLECTION | 01 5. On the write footer: THE MOST PRESTIGIOUS ATTORNEY ACCORDING TO HALVERN & BRISK
Should not have
• information saturation

```html
<!DOCTYPE html>
<html lang="es">
<head>
<meta charset="utf-8">
<title>EL FARO — Brochure para auspiciadores</title>
<link href="https://fonts.googleapis.com/css2?family=Montserrat:wght@300;400;600;700;800&family=Playfair+Display:wght@800;900&display=swap" rel="stylesheet">
<style>
  :root{
    --backdrop:#8d8d8f;
    --paper:#f4f4f4;
    --paper-shade:#e9e9ea;
    --slate:#6d6f72;
    --slate-dark:#4a4c4f;
    --ink:#2b2b2b;
    --muted:#8a8a8a;
    --teal:#2f7f86;
    --format-fill:#dfe5e8;
    --row:#e2e2e2;
    --white:#ffffff;
  }
  *{box-sizing:border-box;margin:0;padding:0}
  html,body{width:1200px;height:1200px;overflow:hidden}
  body{background:var(--backdrop);font-family:"Montserrat",sans-serif;color:var(--ink);position:relative}

  .spread{position:absolute;left:50px;width:1100px;height:550px;display:flex;box-shadow:0 10px 30px rgba(0,0,0,.25)}
  .spread--rates{top:33px}
  .spread--covers{top:617px}
  .page{position:relative;width:550px;height:550px;overflow:hidden}
  .page--light{background:var(--paper)}
  .page--light + .page--light{background:linear-gradient(90deg,var(--paper-shade),var(--paper) 12%)}
  .page--slate{background:linear-gradient(90deg,#5f6164,var(--slate) 10%)}

  /* formats grid */
  .formats{position:absolute;left:40px;top:40px;width:470px;display:grid;grid-template-columns:repeat(3,1fr);row-gap:26px;column-gap:14px}
  .format{display:flex;flex-direction:column;align-items:center;gap:8px}
  .format-sheet{display:flex;height:78px;box-shadow:0 1px 3px rgba(0,0,0,.15)}
  .format-sheet span{width:58px;height:78px;background:var(--white);border:1px solid #d7dadc}
  .format-sheet span.is-ad{background:var(--format-fill)}
  .format-sheet span.is-third{width:20px;background:var(--format-fill)}
  .format-sheet .third-wrap{display:flex;width:58px;background:var(--white);border:1px solid #d7dadc}
  .format-label{font-size:9px;color:var(--muted);text-align:center;line-height:1.3}
  .format-label strong{color:var(--ink);font-weight:700;display:block}

  /* rate table */
  .rates{position:absolute;left:40px;top:318px;width:470px;border-collapse:separate;border-spacing:0 3px;font-size:10px}
  .rates th{background:var(--teal);color:var(--white);font-weight:400;padding:4px 8px;text-align:left}
  .rates td{padding:3px 8px}
  .rates td:first-child{background:var(--row);color:var(--muted)}
  .rates td.num{font-weight:700;color:var(--ink)}
  .rates-note{position:absolute;left:228px;top:512px;font-size:9px;color:var(--teal)}

  /* cover */
  .cover{position:absolute;overflow:hidden;box-shadow:0 6px 16px rgba(0,0,0,.3);border:6px solid var(--white)}
  .cover-photo{position:absolute;inset:0}
  .cover-masthead{position:absolute;left:6px;top:8px;writing-mode:vertical-rl;transform:rotate(180deg);font-weight:800;color:var(--white);letter-spacing:.04em;line-height:1}
  .cover-headline{position:absolute;font-family:"Playfair Display",serif;font-weight:900;color:var(--white);line-height:1.02}
  .tone-gold .cover-photo{background:linear-gradient(160deg,#cfc6b2 0%,#c9a13a 40%,#a8702f 70%,#4b3c32 100%)}
  .tone-teal .cover-photo{background:linear-gradient(160deg,#5c7f8c 0%,#2f8d98 45%,#2d4f63 100%)}
  .tone-violet .cover-photo{background:linear-gradient(160deg,#8b8c96 0%,#7a5a9c 45%,#3f3450 100%)}
  .tone-sky .cover-photo{background:linear-gradient(160deg,#cfd6da 0%,#5c8fa6 40%,#7d8a3a 80%,#4d5a2d 100%)}

  .cover--feature{left:70px;top:60px;width:300px;height:390px}
  .cover--feature .cover-masthead{font-size:58px}
  .cover--feature .cover-headline{left:70px;bottom:28px;font-size:27px;width:210px}

  .founders{position:absolute;left:370px;top:150px;width:160px;height:210px;background:var(--slate);padding:14px 12px;color:#e6e6e6;font-size:8.5px;line-height:1.45}
  .founders strong{color:var(--white)}
  .founders-photo{margin-top:10px;height:56px;border-radius:2px;background:linear-gradient(90deg,#3d3f42,#9a9a9a 60%,#cfc7bd)}

  /* back page */
  .back-photo{position:absolute;inset:0;background:linear-gradient(135deg,#2d2a27 0%,#5b5753 35%,#9d9b98 52%,#c9c9c9 62%,#3c3c3c 80%,#242424 100%)}
  .cover--held{left:120px;top:70px;width:250px;height:320px}
  .cover--held .cover-masthead{font-size:48px}
  .cover--held .cover-headline{left:64px;top:80px;font-size:24px;width:170px}
  .contact{position:absolute;right:40px;bottom:40px;text-align:right;color:#e2e2e2;font-size:10px;line-height:1.5;font-style:italic}
  .contact .contact-title{font-style:normal;font-weight:600}
  .contact .contact-web{font-weight:700;color:var(--white)}

  /* covers collection */
  .collection{position:absolute;left:36px;top:46px;display:grid;grid-template-columns:repeat(2,180px);gap:14px}
  .collection .cover{position:relative;width:180px;height:228px;border-width:5px}
  .collection .cover-masthead{font-size:34px}
  .collection .cover-headline{left:44px;top:58px;font-size:17px;width:122px}
  .brand{position:absolute;right:36px;top:40px;writing-mode:vertical-rl;font-weight:800;font-size:50px;color:var(--white);letter-spacing:.06em;line-height:1}
  .intro{position:absolute;left:436px;top:350px;width:84px;font-size:8px;line-height:1.5;color:#d7d7d7;font-weight:300}
</style>
</head>
<body>

<section class="spread spread--rates">
  <div class="page page--light">
    <div class="formats">
      <div class="format"><div class="format-sheet"><span></span><span class="is-ad"></span></div><p class="format-label">Contraportada</p></div>
      <div class="format"><div class="format-sheet"><span class="is-ad"></span><span class="is-ad"></span></div><p class="format-label">Contraportada + Página</p></div>
      <div class="format"><div class="format-sheet"><span></span><span class="is-ad"></span></div><p class="format-label">Página Completa</p></div>
      <div class="format"><div class="format-sheet"><span class="is-ad"></span><span class="is-ad"></span></div><p class="format-label">Dos Páginas Interiores</p></div>
      <div class="format"><div class="format-sheet"><span></span><div class="third-wrap"><span class="is-third"></span></div></div><p class="format-label">1/3 de Página Vertical</p></div>
      <div class="format"><div class="format-sheet"><span></span><span class="is-ad"></span></div><p class="format-label"><strong>Branded Content</strong>Sección Auspiciada<br>por Marca - Presencia</p></div>
    </div>
    <table class="rates">
      <thead><tr><th></th><th>Valor Unitario</th><th>Valor por 6 Números</th></tr></thead>
      <tbody>
        <tr><td>Contraportada</td><td class="num">1.800.000</td><td class="num">9.600.000</td></tr>
        <tr><td>Contraportada + Página</td><td class="num">3.000.000</td><td class="num">16.000.000</td></tr>
        <tr><td>Página Completa</td><td class="num">1.300.000</td><td class="num">6.600.000</td></tr>
        <tr><td>Dos Páginas Interiores</td><td class="num">2.500.000</td><td class="num">14.000.000</td></tr>
        <tr><td>1/3 de Página Vertical</td><td class="num">700.000</td><td class="num">4.000.000</td></tr>
        <tr><td>Branded Content</td><td class="num">1.000.000</td><td class="num">4.800.000</td></tr>
      </tbody>
    </table>
    <p class="rates-note">*Valores No Incluyen IVA</p>
  </div>

  <div class="page page--light">
    <div class="cover cover--feature tone-gold">
      <div class="cover-photo" role="img" aria-label="Retrato de una abogada con gafas oscuras, tratado en duotono dorado"></div>
      <p class="cover-masthead">EL FARO</p>
      <h2 class="cover-headline">El management en los Estudios de abogados</h2>
    </div>
    <aside class="founders">
      <p>Detrás del proyecto EL FARO está <strong>Tomás Errázuriz</strong>, abogado y máster en Derecho de la Empresa, con más de diez años de experiencia; y <strong>Javiera Montt</strong>, periodista experta en comunicación corporativa y estrategia para estudios de abogados.</p>
      <div class="founders-photo" role="img" aria-label="Fotografía de los dos fundadores de la revista"></div>
    </aside>
  </div>
</section>

<section class="spread spread--covers">
  <div class="page">
    <div class="back-photo" role="img" aria-label="Fotografía en blanco y negro de un abogado sosteniendo la revista"></div>
    <div class="cover cover--held tone-sky">
      <div class="cover-photo" role="img" aria-label="Retrato de una abogada en duotono verde y azul"></div>
      <p class="cover-masthead">EL FARO</p>
      <h2 class="cover-headline">¿A dónde se van a estudiar los mejores abogados del mundo?</h2>
    </div>
    <address class="contact">
      <span class="contact-title">Contacto</span><br>
      Tomás Errázuriz +56 9 4120 7731<br>
      Javiera Montt +56 9 5380 2264<br>
      <span class="contact-web">www.revistaelfaro.cl</span>
    </address>
  </div>

  <div class="page page--slate">
    <div class="collection">
      <div class="cover tone-teal">
        <div class="cover-photo" role="img" aria-label="Retrato de un abogado en duotono turquesa"></div>
        <p class="cover-masthead">EL FARO</p>
        <h2 class="cover-headline">La nueva ley que vendrá en ciberseguridad</h2>
      </div>
      <div class="cover tone-violet">
        <div class="cover-photo" role="img" aria-label="Retrato de un abogado en duotono violeta"></div>
        <p class="cover-masthead">EL FARO</p>
        <h2 class="cover-headline">El abogado que triunfó en la Haya</h2>
      </div>
      <div class="cover tone-gold">
        <div class="cover-photo" role="img" aria-label="Retrato de una abogada con gafas oscuras en duotono dorado"></div>
        <p class="cover-masthead">EL FARO</p>
        <h2 class="cover-headline">El management en los Estudios de abogados</h2>
      </div>
      <div class="cover tone-sky">
        <div class="cover-photo" role="img" aria-label="Retrato de una abogada en duotono verde y azul"></div>
        <p class="cover-masthead">EL FARO</p>
        <h2 class="cover-headline">¿A dónde se van a estudiar los mejores abogados del mundo?</h2>
      </div>
    </div>
    <h1 class="brand">EL FARO</h1>
    <p class="intro">Te presentamos una nueva revista de carácter legal para abogados de la nueva escuela, con una forma de pensar moderna, diferente y vanguardista. Una revista que estará presente en los escenarios más importantes del país: boutiques y grandes firmas legales.</p>
  </div>
</section>

</body>
</html>
```